New Generation Winery needs inspiring label for special bottling

We are a family owned winery in the Rhine Valley in Germany. Check www.brendel-aumann.de . We have a very exciting project going: In 2014 we harvested our best vinyard and split the grapes in half. First half I have treated the way I have done it over the past 40 years. Second half I gave to my daughter who is just entering the winemaking business. She has treated it in a completely different way - her way - the way of the new generation. One of the differentiators; she has squeezed the juices with her bare feet which reduces acidity and bitterness in the wine (less tannins). This is why we want to call the wine "Mondgrüße" (meaning "Moongreets"). Please be careful when writing the "ß" . It is a German letter which replaces the "double s". It is NOT a capital B!! I Have attached a file which gives you the size of the label and another file which shows the current design of the winery labels. If possible it should pick up some elements from the current design (maybe just the colours?) but otherwise you are free. It will go on a dark green bottle, almost black. Apart from the word "Mondgrüße" you need to place the grape "Riesling", the word "trocken" (means dry) and the year of the harvest "2014".

Industry/Entity Type

Brendel

Requirements
Nice to have
• Update 25.3.2015: Have a look at the attached image "Inspiration". Maybe that is a good thought starter, too. Have fun..

```html
<!DOCTYPE html>
<html lang="de">
<head>
<meta charset="utf-8">
<title>Mondgrüße Riesling 2014 – Etiketten</title>
<link rel="stylesheet" href="https://fonts.googleapis.com/css2?family=Oswald:wght@500&family=Pinyon+Script&family=Montserrat:wght@500&display=swap">
<style>
  :root {
    --page: #ffffff;
    --label-white: #f7f7f6;
    --label-cream: #f3efe1;
    --frame-line: #d8d2bf;
    --ink: #3b3b3d;
    --ink-soft: #4a4a4a;
  }
  * { box-sizing: border-box; margin: 0; padding: 0; }
  html, body { width: 886px; height: 1200px; overflow: hidden; background: var(--page); }
  .label-row {
    position: absolute; top: 613px; left: 40px;
    display: flex; gap: 34px;
  }
  .label {
    position: relative; width: 248px; height: 295px; overflow: hidden;
    box-shadow: 0 1px 4px rgba(0,0,0,.18);
  }
  .label--white { background: var(--label-white); }
  .label--cream { background: var(--label-cream); }
  .label__frame {
    position: absolute; inset: 12px;
    border: 1px solid var(--frame-line);
    box-shadow: inset 0 0 0 3px var(--label-cream), inset 0 0 0 4px var(--frame-line);
  }
  .wine-name {
    position: absolute; left: 0; right: 0; text-align: center;
    font-family: "Oswald", sans-serif; font-weight: 500;
    color: var(--ink); letter-spacing: .5px; line-height: 1;
  }
  .grape {
    position: absolute; left: 0; right: 0; text-align: center;
    font-family: "Pinyon Script", cursive; color: var(--ink); line-height: 1;
  }
  .vintage, .style {
    position: absolute; font-family: "Montserrat", sans-serif;
    color: var(--ink-soft); line-height: 1; letter-spacing: 1px;
  }

  .label--white .wine-name { top: 86px; font-size: 38px; }
  .label--white .vintage, .label--white .style { left: 0; right: 0; text-align: center; }
  .label--white .vintage { top: 176px; font-size: 12px; letter-spacing: 2px; }
  .label--white .grape { top: 206px; font-size: 26px; }
  .label--white .style { top: 257px; font-size: 9px; }

  .label--cream .wine-name { font-size: 40px; }
  .label--cream .grape { font-size: 36px; }
  .label--cream .vintage { left: 93px; font-size: 12px; }
  .label--cream .style { left: 62px; font-size: 9px; }

  .label--b .wine-name { top: 64px; }
  .label--c .wine-name { top: 44px; }
  .label--cream .grape { top: 176px; }
  .label--cream .vintage { top: 234px; }
  .label--cream .style { top: 250px; }
</style>
</head>
<body>
  <main class="label-row">
    <section class="label label--white">
      <h1 class="wine-name">Mondgrüße</h1>
      <p class="vintage">2014</p>
      <p class="grape">Riesling</p>
      <p class="style">TROCKEN</p>
    </section>

    <section class="label label--cream label--b">
      <div class="label__frame"></div>
      <h1 class="wine-name">Mondgrüße</h1>
      <p class="grape">Riesling</p>
      <p class="vintage">2014</p>
      <p class="style">TROCKEN</p>
    </section>

    <section class="label label--cream label--c">
      <div class="label__frame"></div>
      <h1 class="wine-name">Mondgrüße</h1>
      <p class="grape">Riesling</p>
      <p class="vintage">2014</p>
      <p class="style">TROCKEN</p>
    </section>
  </main>
</body>
</html>
```